Awesome photographers card for an awesome new business

Double sided business card Black background and silver logo in middle on one side. Details on otherside. please keep it simple

Photographer

Gavin Tolley
0482615073
GavinTolleyPhotography82@lumenpost.com
www.GavinTolleyPhotography.com.au
Instagram _Gavin_tolley

Requirements
Must have
• My logo in Silver
• please use instagram logo instead of "Instagram"

```html
<!DOCTYPE html>
<html lang="en">
<head>
<meta charset="utf-8">
<title>Gavin Tolley Photography – Business Card</title>
<link href="https://fonts.googleapis.com/css2?family=Nunito:wght@400;600;700&display=swap" rel="stylesheet">
<style>
  :root {
    --backdrop: #e6e4e1;
    --card-black: #0b0b0b;
    --silver: #cfcfcf;
    --silver-soft: #b8b8b8;
    --shadow: rgba(0, 0, 0, 0.35);
  }
  * { margin: 0; padding: 0; box-sizing: border-box; }
  html, body {
    width: 1200px;
    height: 1000px;
    overflow: hidden;
    background: var(--backdrop);
    font-family: "Nunito", "Helvetica Neue", Arial, sans-serif;
  }
  .canvas {
    position: relative;
    width: 1200px;
    height: 1000px;
  }
  .card {
    position: absolute;
    left: 267px;
    width: 665px;
    height: 397px;
    background: var(--card-black);
    box-shadow: 0 4px 14px var(--shadow);
    color: var(--silver);
  }
  .card--front { top: 74px; }
  .card--back { top: 533px; }

  /* Front: brand name set as plain text with one plain circle */
  .brand {
    position: absolute;
    inset: 0;
    display: flex;
    align-items: center;
    justify-content: center;
    gap: 16px;
  }
  .brand__dot {
    width: 22px;
    height: 22px;
    border-radius: 50%;
    background: var(--silver);
  }
  .brand__name {
    font-size: 30px;
    font-weight: 600;
    letter-spacing: 6px;
    text-transform: uppercase;
    color: var(--silver);
  }

  /* Back: contact details */
  .details {
    position: absolute;
    left: 0;
    right: 0;
    top: 98px;
    text-align: center;
  }
  .details__name {
    font-size: 19px;
    font-weight: 700;
    letter-spacing: 0.5px;
    text-transform: uppercase;
    color: var(--silver);
    line-height: 24px;
  }
  .details__role {
    font-size: 15px;
    font-weight: 400;
    color: var(--silver-soft);
    line-height: 20px;
  }
  .details__contact {
    margin-top: 34px;
    font-size: 15px;
    line-height: 26px;
    color: var(--silver);
  }
  .details__social {
    margin-top: 8px;
    display: flex;
    flex-direction: column;
    align-items: center;
    gap: 5px;
    font-size: 15px;
    color: var(--silver);
  }
  .details__social-mark {
    width: 10px;
    height: 10px;
    background: var(--silver-soft);
  }
</style>
</head>
<body>
  <main class="canvas">
    <section class="card card--front" aria-label="Card front">
      <div class="brand">
        <span class="brand__dot"></span>
        <span class="brand__name">Gavin Tolley</span>
      </div>
    </section>

    <section class="card card--back" aria-label="Card back">
      <div class="details">
        <p class="details__name">Gavin Tolley</p>
        <p class="details__role">Photographer</p>
        <div class="details__contact">
          <p>0482615073</p>
          <p>GavinTolleyPhotography82@lumenpost.com</p>
          <p>www.GavinTolleyPhotography.com.au</p>
        </div>
        <div class="details__social">
          <span class="details__social-mark"></span>
          <span>_Gavin_tolley</span>
        </div>
      </div>
    </section>
  </main>
</body>
</html>
```